Business Card/ Email Signature Design Project

I am an Interior Designer. I need a business card that looks sophisticated stylish but simple in design. My work covers space design/ interior architecture/ furniture design/ product development & styling.

I have a very specific brief and know mostly what I want. I'm hoping to work with someone who can translate my ideas.

My branding should have a strong focus on my name, the majority of my work is referral based.
I'm keen to keep a monochromatic colour scheme: dark charcoal/ black/ white/ embossing/ silver. I'm not suggesting we use all that I've listed, they are possible ideas at this stage. I will need to be mindful of printing costs an also how I make the design work across, cards, letter heads, email logo and web design.

Theory behind images sent below;
1-Rug Image_(minus boarder) I was thinking this image could be used on the back of the card with my contact details over. I like that the lines are almost hand drawn and start to look free form. It's a subtle contrast to a more formal front of the card with my name.
2_Owen Ratley_I really like the orientation, the proportion of font on the card, the colour and the font. I like the lower case for my name and the upper case for 'Interior Design'. Not sure if it should be 'Interior Designer or Interior Design' at this stage, was leaning towards 'Interior Design'. Was thinking the 'i' and 'd' in my surname could be the colour eg 'silver'?? We can decide on this once we see it.

Look forward to hearing from you.
Cheers,
Noreen Bastoli

Industry/Entity Type

Printing

Logo Text

Noreen Bastoli Interior Design

```html
<!DOCTYPE html>
<html lang="en">
<head>
<meta charset="utf-8">
<title>Noreen Bastoli Interior Design – Business Card</title>
<link rel="stylesheet" href="https://fonts.googleapis.com/css2?family=Open+Sans:wght@400;600&display=swap">
<style>
  :root {
    --backdrop: #2b2b2b;
    --card-black: #0c0c0c;
    --card-charcoal: #2a2a2a;
    --silver: #d4d6d8;
    --caption-grey: #8c8c8c;
    --rug-light: #b08e5e;
    --rug-mid: #8f6f44;
    --rug-dark: #6b5232;
    --contact-white: #ffffff;
  }
  * { box-sizing: border-box; margin: 0; padding: 0; }
  html, body {
    width: 1200px;
    height: 900px;
    overflow: hidden;
  }
  body {
    background: var(--backdrop);
    font-family: "Open Sans", Arial, sans-serif;
    position: relative;
  }
  .card {
    position: absolute;
    width: 560px;
    height: 330px;
    box-shadow: 0 14px 30px rgba(0, 0, 0, 0.55);
    overflow: hidden;
  }
  .card-front {
    left: 70px;
    top: 80px;
    background: radial-gradient(ellipse at 55% 50%, var(--card-charcoal) 0%, var(--card-black) 75%);
  }
  .brand {
    position: absolute;
    left: 150px;
    top: 128px;
  }
  .brand-name {
    font-size: 46px;
    font-weight: 400;
    color: var(--silver);
    letter-spacing: 0.5px;
    line-height: 1;
    text-transform: lowercase;
  }
  .brand-tagline {
    margin-top: 6px;
    margin-left: 6px;
    font-size: 13px;
    letter-spacing: 9px;
    color: var(--caption-grey);
    text-transform: uppercase;
  }
  .card-back {
    left: 590px;
    top: 480px;
  }
  .rug-texture {
    position: absolute;
    inset: 0;
    background: linear-gradient(135deg, var(--rug-light) 0%, var(--rug-mid) 55%, var(--rug-dark) 100%);
  }
  .contact-list {
    position: absolute;
    left: 26px;
    bottom: 22px;
    list-style: none;
    color: var(--contact-white);
    font-size: 16px;
    line-height: 1.25;
    text-shadow: 0 1px 2px rgba(0, 0, 0, 0.35);
  }
</style>
</head>
<body>
  <section class="card card-front" aria-label="Card front">
    <div class="brand">
      <h1 class="brand-name">noreen bastoli</h1>
      <p class="brand-tagline">Interior Design</p>
    </div>
  </section>

  <section class="card card-back" aria-label="Card back">
    <div class="rug-texture" role="img" aria-label="Golden woven rug texture with free-form hand-drawn black lines"></div>
    <ul class="contact-list">
      <li>Adress: P.O Box 412 Northcote VIC. 3070</li>
      <li>Email: interiors@noreenbastoli.com</li>
      <li>Web: www.noreenbastoli.com</li>
      <li>Mobile: 0400 555 019</li>
    </ul>
  </section>
</body>
</html>
```